Wine Label for a Sweet Wine Called "Glimmo"

We need a wine label that will be used for both a sweet red and a sweet white wine. The very important thing to remember is the target market for these wines is: young American women who love sweet wines and they also spend a lot of their money on their hair, clothes, jewelry, nails. They LOVE Glimmo (Glimmo is a word used to describe flashy accessories, jewelry, decoration.) This label needs to be eye catching, showy, fun, glittery. Please put the brand name, "Glimmo," big, and then in smaller but still readable words underneath the label or somewhere on the label: Sweet, Sophisticated, Red (or white). (An example of what I mean is attached). To differentiate between the two color wines you can suggest color changes to differentiate between the red label and the white label but the label design itself should be the same. Ultimately, the label can be the exact same label for both white and red as long as it looks good on a white wine (a greenish/yellow wine in a clear glass bottle) and a red wine (a dark color wine in a dark bottle).

I've attached an example of the text size relationship between the word Glimmo and the words to go underneath or elsewhere on the label, but you can certainly play with this-- it is just a suggestion of the text size relationship, and definitely NOT at all mandatory that you use any of these fonts.

You can pick the size of the label but try to stay within normal wine label sizes, meaning don't go bigger than approx. 3.5 inches wide and 5 inches tall.

Target Market(s)

Young American women who love sweet wines and spend a lot of money on their hair, clothes, jewelry, nails. They love Glimmo (Glimmo is a word that means flashy accessories, jewelry, decoration)

Requirements
Must have
• It needs to be flashy, glittery, fun, eye catching, memorable
Nice to have
• It shouldn't be too too ultra feminine! The target market is strong independent women and we also have men who will buy it too.

```html
<!DOCTYPE html>
<html lang="en">
<head>
<meta charset="utf-8">
<title>Glimmo Wine Label Concepts</title>
<link rel="stylesheet" href="https://fonts.googleapis.com/css2?family=Rye&family=Cinzel:wght@400;700;900&family=Playfair+Display:wght@500&display=swap">
<style>
  :root {
    --ink: #000000;
    --paper: #ffffff;
    --gold: #dcbd7e;
    --gold-deep: #a8894a;
    --gold-soft: rgba(220, 189, 126, 0.55);
    --grey: #7c7668;
    --gold-text: linear-gradient(90deg, #7f7868 0%, #cfb57c 35%, #e6c88a 60%, #cdb27a 80%, #8d8574 100%);
  }
  html, body { margin: 0; padding: 0; }
  body {
    width: 1200px; height: 1200px; overflow: hidden;
    background: var(--paper); position: relative;
  }
  .label { position: absolute; background: var(--ink); overflow: hidden; }
  .label--deco { left: 52px; top: 24px; width: 526px; height: 552px; }
  .label--baroque { left: 629px; top: 24px; width: 522px; height: 552px; }
  .label--badge { left: 334px; top: 600px; width: 532px; height: 550px; }

  /* Corner frames: dotted outer rule, solid inner rule, flat ornament block */
  .corner { position: absolute; width: 118px; height: 118px; }
  .corner::before, .corner::after { content: ""; position: absolute; }
  .corner::before { inset: 0; border-top: 3px dotted var(--gold); border-left: 3px dotted var(--gold); }
  .corner::after { left: 8px; top: 8px; width: 96px; height: 96px; border-top: 1px solid var(--gold-deep); border-left: 1px solid var(--gold-deep); }
  .corner--tl { left: 8px; top: 8px; }
  .corner--tr { right: 8px; top: 8px; transform: scaleX(-1); }
  .corner--bl { left: 8px; bottom: 8px; transform: scaleY(-1); }
  .corner--br { right: 8px; bottom: 8px; transform: scale(-1, -1); }
  .corner__ornament {
    position: absolute; left: 20px; top: 20px; width: 44px; height: 44px;
    border-radius: 0 0 44px 0;
    background: linear-gradient(135deg, var(--gold) 0%, var(--gold-deep) 100%);
    opacity: 0.6;
  }

  .frame { position: absolute; left: 0; top: 0; }

  .brand {
    position: absolute; left: 0; right: 0; margin: 0; text-align: center;
    background: var(--gold-text); -webkit-background-clip: text; background-clip: text;
    color: transparent; line-height: 1; white-space: nowrap;
  }
  .brand--deco { font-family: "Rye", serif; font-weight: 400; font-size: 60px; top: 236px; }
  .brand--baroque { font-family: "Cinzel", serif; font-weight: 900; font-size: 62px; top: 236px; letter-spacing: 2px; }
  .brand--badge { font-family: "Rye", serif; font-weight: 400; font-size: 70px; top: 240px; }

  .variant-plaque {
    position: absolute; left: 168px; top: 314px; width: 190px; height: 36px;
    background: linear-gradient(90deg, #8a826f, #d8bc80 50%, #8a826f);
    display: flex; align-items: center; justify-content: center;
    font-family: "Cinzel", serif; font-weight: 900; font-size: 24px; line-height: 1;
    color: var(--ink); letter-spacing: 2px;
  }
  .variant-ribbon {
    position: absolute; left: 214px; top: 177px; width: 104px; text-align: center;
    font-family: "Cinzel", serif; font-weight: 400; font-size: 13px; line-height: 18px;
    color: var(--gold); letter-spacing: 2px;
  }

  .tagline {
    position: absolute; left: 0; right: 0; margin: 0; text-align: center;
    background: var(--gold-text); -webkit-background-clip: text; background-clip: text;
    color: transparent; white-space: nowrap; line-height: 1;
  }
  .tagline--caps { font-family: "Cinzel", serif; font-weight: 400; font-size: 14px; letter-spacing: 1.5px; }
  .tagline--deco { top: 492px; }
  .tagline--badge { top: 480px; }
  .tagline--script { font-family: "Playfair Display", serif; font-weight: 500; font-size: 15px; letter-spacing: 1.5px; top: 310px; }

  /* Ornament placeholders: crisp-edged soft fills */
  .fan {
    position: absolute; width: 92px; height: 62px;
    background: linear-gradient(180deg, var(--gold) 0%, var(--gold-deep) 100%);
    opacity: 0.55;
  }
  .fan--top { left: 217px; top: 104px; border-radius: 46px 46px 0 0; }
  .fan--bottom { left: 217px; top: 384px; border-radius: 0 0 46px 46px; }

  .scroll { position: absolute; opacity: 0.6; }
  .scroll--top { left: 118px; top: 18px; width: 286px; height: 196px; border-radius: 50% 50% 40% 40%; background: linear-gradient(180deg, var(--gold) 0%, var(--gold-deep) 100%); }
  .scroll--bottom { left: 118px; top: 338px; width: 286px; height: 196px; border-radius: 40% 40% 50% 50%; background: linear-gradient(0deg, var(--gold) 0%, var(--gold-deep) 100%); }
  .scroll--left { left: 12px; top: 170px; width: 84px; height: 212px; border-radius: 42px; background: linear-gradient(90deg, #5c584e 0%, var(--grey) 100%); }
  .scroll--right { right: 12px; top: 170px; width: 84px; height: 212px; border-radius: 42px; background: linear-gradient(270deg, #5c584e 0%, var(--grey) 100%); }

  .crest { position: absolute; left: 238px; top: 206px; width: 56px; height: 22px; border-radius: 3px; background: linear-gradient(180deg, var(--gold), var(--gold-deep)); opacity: 0.7; }
  .flourish { position: absolute; left: 230px; top: 354px; width: 72px; height: 20px; border-radius: 0 0 36px 36px; background: linear-gradient(180deg, var(--gold), var(--gold-deep)); opacity: 0.55; }
</style>
</head>
<body>

<section class="label label--deco" aria-label="Glimmo label, art deco frame">
  <div class="corner corner--tl"><div class="corner__ornament" role="img" aria-label="Gold corner flourish"></div></div>
  <div class="corner corner--tr"><div class="corner__ornament" role="img" aria-label="Gold corner flourish"></div></div>
  <div class="corner corner--bl"><div class="corner__ornament" role="img" aria-label="Gold corner flourish"></div></div>
  <div class="corner corner--br"><div class="corner__ornament" role="img" aria-label="Gold corner flourish"></div></div>
  <svg class="frame" width="526" height="552" viewBox="0 0 526 552" aria-hidden="true">
    <defs>
      <linearGradient id="deco-gold" x1="0" x2="1">
        <stop offset="0" stop-color="#8a826f"/><stop offset=".5" stop-color="#dcbd7e"/><stop offset="1" stop-color="#8a826f"/>
      </linearGradient>
    </defs>
    <path d="M84 164 L203 164 L203 120 A60 36 0 0 1 323 120 L323 164 L442 164 L442 210 Q478 264 442 318 L442 392 L323 392 L323 432 A60 36 0 0 1 203 432 L203 392 L84 392 L84 318 Q48 264 84 210 Z" fill="none" stroke="url(#deco-gold)" stroke-width="3"/>
    <path transform="translate(263 276) scale(0.93) translate(-263 -276)" d="M84 164 L203 164 L203 120 A60 36 0 0 1 323 120 L323 164 L442 164 L442 210 Q478 264 442 318 L442 392 L323 392 L323 432 A60 36 0 0 1 203 432 L203 392 L84 392 L84 318 Q48 264 84 210 Z" fill="none" stroke="url(#deco-gold)" stroke-width="1.5"/>
    <line x1="74" y1="226" x2="452" y2="226" stroke="url(#deco-gold)" stroke-width="2"/>
    <line x1="74" y1="233" x2="452" y2="233" stroke="url(#deco-gold)" stroke-width="1"/>
    <line x1="74" y1="364" x2="452" y2="364" stroke="url(#deco-gold)" stroke-width="1"/>
    <line x1="74" y1="371" x2="452" y2="371" stroke="url(#deco-gold)" stroke-width="2"/>
    <line x1="150" y1="164" x2="150" y2="226" stroke="url(#deco-gold)" stroke-width="1.5"/>
    <line x1="376" y1="164" x2="376" y2="226" stroke="url(#deco-gold)" stroke-width="1.5"/>
    <line x1="150" y1="371" x2="150" y2="392" stroke="url(#deco-gold)" stroke-width="1.5"/>
    <line x1="376" y1="371" x2="376" y2="392" stroke="url(#deco-gold)" stroke-width="1.5"/>
  </svg>
  <div class="fan fan--top" role="img" aria-label="Gold art deco fan motif"></div>
  <div class="fan fan--bottom" role="img" aria-label="Gold art deco fan motif"></div>
  <h2 class="brand brand--deco">GLIMMO</h2>
  <div class="variant-plaque">WHITE</div>
  <p class="tagline tagline--caps tagline--deco">SWEET | SOPHISTICATED</p>
</section>

<section class="label label--baroque" aria-label="Glimmo label, baroque frame">
  <div class="scroll scroll--top" role="img" aria-label="Ornate gold baroque scrollwork crest"></div>
  <div class="scroll scroll--bottom" role="img" aria-label="Ornate gold baroque scrollwork crest"></div>
  <div class="scroll scroll--left" role="img" aria-label="Silver baroque scrollwork"></div>
  <div class="scroll scroll--right" role="img" aria-label="Silver baroque scrollwork"></div>
  <h2 class="brand brand--baroque">GLIMMO</h2>
  <p class="tagline tagline--script">Sweet | Sophisticated | White</p>
</section>

<section class="label label--badge" aria-label="Glimmo label, badge">
  <div class="corner corner--tl"><div class="corner__ornament" role="img" aria-label="Gold corner flourish"></div></div>
  <div class="corner corner--tr"><div class="corner__ornament" role="img" aria-label="Gold corner flourish"></div></div>
  <div class="corner corner--bl"><div class="corner__ornament" role="img" aria-label="Gold corner flourish"></div></div>
  <div class="corner corner--br"><div class="corner__ornament" role="img" aria-label="Gold corner flourish"></div></div>
  <svg class="frame" width="532" height="550" viewBox="0 0 532 550" aria-hidden="true">
    <defs>
      <linearGradient id="badge-gold" x1="0" x2="1">
        <stop offset="0" stop-color="#8a826f"/><stop offset=".5" stop-color="#dcbd7e"/><stop offset="1" stop-color="#8a826f"/>
      </linearGradient>
    </defs>
    <path d="M120 218 C170 218 190 178 266 158 C342 178 362 218 412 218 A58 58 0 0 1 412 334 C362 334 342 374 266 394 C190 374 170 334 120 334 A58 58 0 0 1 120 218 Z" fill="none" stroke="url(#badge-gold)" stroke-width="2.5"/>
    <path transform="translate(266 276) scale(0.95) translate(-266 -276)" d="M120 218 C170 218 190 178 266 158 C342 178 362 218 412 218 A58 58 0 0 1 412 334 C362 334 342 374 266 394 C190 374 170 334 120 334 A58 58 0 0 1 120 218 Z" fill="none" stroke="url(#badge-gold)" stroke-width="2" stroke-dasharray="1 4" stroke-linecap="round"/>
    <path transform="translate(266 276) scale(0.89) translate(-266 -276)" d="M120 218 C170 218 190 178 266 158 C342 178 362 218 412 218 A58 58 0 0 1 412 334 C362 334 342 374 266 394 C190 374 170 334 120 334 A58 58 0 0 1 120 218 Z" fill="none" stroke="url(#badge-gold)" stroke-width="1"/>
    <path d="M210 174 L322 174 L318 196 L214 196 Z" fill="none" stroke="#dcbd7e" stroke-width="1.5"/>
    <line x1="196" y1="234" x2="336" y2="234" stroke="url(#badge-gold)" stroke-width="1.5"/>
    <line x1="196" y1="326" x2="336" y2="326" stroke="url(#badge-gold)" stroke-width="1.5"/>
    <rect x="196" y="334" width="140" height="10" fill="url(#badge-gold)"/>
  </svg>
  <div class="crest" role="img" aria-label="Small gold crown of spires"></div>
  <div class="flourish" role="img" aria-label="Gold scroll flourish"></div>
  <div class="variant-ribbon">WHITE</div>
  <h2 class="brand brand--badge">GLIMMO</h2>
  <p class="tagline tagline--caps tagline--badge">SWEET | SOPHISTICATED</p>
</section>

</body>
</html>
```